Revamp our software development company Wix site

We need to rework our Wix website theming, layout, design to match our logo file color and theming. There are a few elements we want to keep, such as the top splash 'typing' header.

The current site is hiketoucan.net. This website I created with Wix, but I never fully finished the copy and all sections.

The feel and mood of the site should be "Warm, professional, inviting, and should project expertise in the field, confidence." But not corporate and cold.

The colors and fonts should match the logo theming. The website must match the logo which was designed in a separate contest. So browns, greens, whites, etc. to create a warm and professional, but fun website.

I want to showcase our app development screenshots in a nice, sharp way.

We are a new company, with only a few clients and projects under our belt. So we don't have lots of need for many testimonials, project showcases, etc. just a couple which is why we went with "Recent work" instead of "Portfolio".

It needs a blog section also that looks great, and will allow me to manage the blog after this project is over. The blog's purpose is for SEO content and marketing.

It will be a huge win for the makerbazaar artist, to make something unique that doesn't look like every other templated website.

We can use the text/sections found on hiketoucan.net, then i would like to tweak some of the copy and sections later.

***This is a Wix website*** I think it would be 2 pages. The landing page, then the blog page.

***Awesome inspiration websites/vibes we like***
https://ninekitesworks.com/
https://vostrella.com/
https://www.larkspinmedia.com/
https://www.triplumeworks.com/
https://harbor-makerhaus.com/
https://frostquill.works/

If you have ideas that need to break free from Wix environment, I am open to that idea also. Wix is just easy for a non-technical founder like me to manage our site/blog.

Thanks!

Target Market(s)

Industry leading commercial and residential construction companies seeking custom software development

Industry/Entity Type

We are a boutique software development studio.

Coding

Coded - Design and coding required

Font styles to use
Sans Serif

Requirements
Must have
• Darker/warm background and overall feel. Relaxed and confident vibes. Simplicity, less is more approach. Blog page. Must have project gallery to showcase high res- screenshots. Clear sans serif fonts, nice contrasting colors.
Nice to have
• If it could have some sort of construction related flare, like photos or icon, that could be good, but it cannot be cheesy. A lot of the stock photos of construction workers etc. are terrible and cheesy (please do not use).
Should not have
• lots of pages, music/sounds, busy theming, tiny fonts

```html
<!DOCTYPE html>
<html lang="en">
<head>
<meta charset="utf-8">
<title>Toucan — Custom Software for Builders</title>
<link href="https://fonts.googleapis.com/css2?family=Outfit:wght@300;400;500;600&display=swap" rel="stylesheet">
<style>
:root{
  --espresso:#241811;
  --umber:#322118;
  --lime:#b5d12a;
  --lime-light:#c8e246;
  --mist:#f0f1f2;
  --board:#bfb9b6;
  --muted:#b9aca3;
  --line:#4a3629;
}
*{box-sizing:border-box;margin:0;padding:0}
html,body{width:1200px;height:3650px;overflow:hidden}
body{background:var(--board);font-family:'Outfit',sans-serif;color:var(--mist);position:relative}
.abs{position:absolute}
.accent{color:var(--lime)}

/* brand sheet */
.sheet-logo{left:198px;top:100px;font-size:38px;font-weight:500;color:var(--umber);display:flex;align-items:center;gap:8px}
.sheet-logo .dot{width:22px;height:22px;border-radius:50%;background:var(--lime)}
.sheet-label{font-size:24px;font-weight:500;color:var(--umber)}
.sheet-font{font-size:16px;color:#6f625b;font-weight:300}
.swatch{width:40px;height:40px;border-radius:50%}
.swatch-code{font-size:9px;color:#5d514a;width:50px;text-align:center}

/* site */
.site{left:221px;top:276px;width:795px;height:3273px;background:var(--espresso);overflow:hidden}
.hero-bg{left:0;top:0;width:795px;height:370px;background:#2a1c14}
.brand{display:flex;align-items:center;gap:5px;font-weight:500;color:var(--mist)}
.brand .dot{border-radius:50%;background:var(--lime)}
.nav a{position:absolute;top:18px;font-size:8px;color:var(--mist);text-decoration:none}
.btn-start{left:629px;top:11px;width:91px;height:24px;border:1px solid var(--lime);border-radius:12px;font-size:7.5px;display:flex;align-items:center;justify-content:center;font-weight:500}
.h1{font-size:36px;line-height:39px;font-weight:500;letter-spacing:-.3px}
.h2{font-size:31px;line-height:35px;font-weight:500;letter-spacing:-.3px}
.vert{left:70px;top:227px;font-size:8px;writing-mode:vertical-rl;transform:rotate(180deg);height:58px}
.vert-line{left:78px;top:292px;width:1px;height:24px;background:var(--lime)}
.photo{background:linear-gradient(135deg,#8d8884,#3b3634)}
.pill{left:102px;top:227px;width:147px;height:86px;border-radius:43px;border:2px solid var(--mist)}

.panel{background:var(--umber);border-radius:4px}
.svc-title{left:75px;font-size:13px;font-weight:500}
.svc-text{left:495px;width:232px;font-size:8.5px;line-height:12.5px;color:var(--muted);font-weight:300}
.divider{left:75px;width:645px;height:1px;background:var(--line)}

.card{top:1006px;width:198px;height:198px;border:1px solid var(--line);border-radius:3px;padding:22px 19px}
.card.feature{background:var(--lime);border-color:var(--lime);color:var(--umber)}
.card h3{margin-top:18px;font-size:14px;font-weight:500}
.card p{margin-top:8px;font-size:8px;line-height:13.5px;color:var(--muted);font-weight:300}
.card.feature p{color:#3b2a1d}

.tag{display:inline-block;border:1px solid var(--muted);border-radius:8px;font-size:6px;padding:2px 7px;letter-spacing:.5px;margin-right:4px;text-transform:uppercase}
.work-title{left:75px;top:1460px;font-size:17px;line-height:22px;font-weight:400}
.work-text{left:75px;top:1536px;width:300px;font-size:8.5px;line-height:13px;color:var(--muted);font-weight:300}
.features{left:75px;top:1590px;display:flex;gap:14px;font-size:7.5px}
.features span{display:flex;align-items:center;gap:4px}
.arrow-btn{top:1620px;width:30px;height:18px;border-radius:9px;border:1px solid var(--lime);display:flex;align-items:center;justify-content:center}
.arrow-btn.on{background:var(--lime)}

.client{top:1834px;font-size:11px;color:#7a6a5f;letter-spacing:1px;display:flex;align-items:center;gap:5px;font-weight:500}
.client i{width:14px;height:14px;border-radius:50%;border:1.5px solid #7a6a5f;display:block}

.quote-box{left:159px;top:1911px;width:610px;height:276px;background:var(--lime)}
.quote-text{left:269px;top:1958px;width:466px;font-size:9.3px;line-height:17.6px;color:#3b2a1d;font-weight:300}
.quote-name{left:269px;top:2124px;font-size:11px;color:var(--umber);font-weight:500}

.mini-tag{font-size:6px;color:var(--lime);letter-spacing:.5px;text-transform:uppercase;display:flex;align-items:center;gap:4px}
.mini-tag .tag{color:var(--mist);font-size:5.5px;padding:1px 5px}
.post-side{left:432px;width:288px;height:120px;border:1px solid var(--line);border-radius:3px}
.post-side .thumb{left:13px;top:13px;width:93px;height:93px}
.post-side .txt{left:118px;top:25px;width:160px}
.post-side h4{margin-top:6px;font-size:14px;line-height:17.5px;font-weight:400}

.field{font-size:9px;display:flex;align-items:flex-end;gap:6px}
.field b{font-weight:400}
.field .rule{flex:1;height:1px;background:var(--muted);margin-bottom:3px}
.go{left:361px;top:2913px;width:74px;height:74px;border-radius:50%;background:var(--lime);color:var(--umber);font-size:8px;display:flex;flex-direction:column;align-items:center;justify-content:center;gap:3px;font-weight:500}

.f-col{top:3134px;width:140px;text-align:center}
.f-col h5{font-size:11px;font-weight:500}
.f-col p{font-size:7.5px;line-height:12px;color:var(--muted);font-weight:300;margin-top:5px}
.social{top:3203px;width:19px;height:19px;border-radius:50%;border:1px solid var(--muted)}
.foot-small{top:3207px;font-size:6.5px;color:var(--muted)}
</style>
</head>
<body>

<!-- brand sheet -->
<div class="abs sheet-logo"><span class="dot"></span>Toucan</div>
<div class="abs sheet-label" style="left:538px;top:101px">Fonts:</div>
<div class="abs sheet-font" style="left:538px;top:145px">Outfit Sans</div>
<div class="abs sheet-label" style="left:789px;top:101px">Colors:</div>
<div class="abs swatch" style="left:790px;top:139px;background:#241811"></div>
<div class="abs swatch" style="left:843px;top:139px;background:#322118"></div>
<div class="abs swatch" style="left:894px;top:139px;background:#b5d12a"></div>
<div class="abs swatch" style="left:945px;top:139px;background:#c8e246"></div>
<div class="abs swatch" style="left:996px;top:139px;background:#f0f1f2"></div>
<div class="abs swatch-code" style="left:785px;top:188px">#241811</div>
<div class="abs swatch-code" style="left:838px;top:188px">#322118</div>
<div class="abs swatch-code" style="left:889px;top:188px">#b5d12a</div>
<div class="abs swatch-code" style="left:940px;top:188px">#c8e246</div>
<div class="abs swatch-code" style="left:991px;top:188px">#f0f1f2</div>

<main class="abs site">
  <div class="abs hero-bg"></div>

  <!-- nav -->
  <div class="abs brand" style="left:75px;top:15px;font-size:17px"><span class="dot" style="width:10px;height:10px"></span>Toucan</div>
  <nav class="nav">
    <a style="left:265px">Home</a><a style="left:312px">What We Do</a><a style="left:378px">Meet Toucan</a><a style="left:452px">Projects</a><a style="left:503px">Blog</a>
  </nav>
  <div class="abs btn-start">Start Your Project</div>

  <!-- hero -->
  <h1 class="abs h1" style="left:75px;top:92px">Take Your<br><span class="accent">Cost Control</span><br>to the Next Level</h1>
  <div class="abs vert">How We Help?</div>
  <div class="abs vert-line"></div>
  <div class="abs pill photo" role="img" aria-label="Hands typing on a laptop showing code"></div>
  <svg class="abs" style="left:437px;top:78px" width="358" height="256" viewBox="0 0 358 256" role="img" aria-label="Construction engineer in hard hat and high-vis vest holding a tablet">
    <defs>
      <linearGradient id="heroPhoto" x1="0" y1="0" x2="1" y2="1"><stop offset="0" stop-color="#d7d4d0"/><stop offset=".6" stop-color="#7b7772"/><stop offset="1" stop-color="#3d3a37"/></linearGradient>
      <clipPath id="heroClip"><rect width="358" height="256"/></clipPath>
    </defs>
    <g clip-path="url(#heroClip)">
      <ellipse cx="176" cy="138" rx="180" ry="150" fill="var(--lime)"/>
      <ellipse cx="196" cy="132" rx="180" ry="150" fill="url(#heroPhoto)"/>
      <rect x="196" y="0" width="162" height="256" fill="url(#heroPhoto)"/>
    </g>
  </svg>

  <!-- intro -->
  <h2 class="abs h2" style="left:75px;top:411px">We Help Leading Builders<br><span class="accent">Break Free</span> From<br>Off-the-Shelf Software</h2>

  <section class="abs panel" style="left:25px;top:547px;width:744px;height:347px"></section>
  <div class="abs svc-title" style="top:590px"><span class="accent">01</span> / Tailor</div>
  <p class="abs svc-text" style="top:587px">Research shows that less than 10% of software features are frequently used, leaving many bells and whistles unclicked. We'll tailor to fit and eliminate this waste.</p>
  <div class="abs divider" style="top:665px"></div>
  <div class="abs svc-title" style="top:689px"><span class="accent">02</span> / Empower</div>
  <p class="abs svc-text" style="top:686px">When your team has tailored tools, they'll work happier, faster, and more effectively towards your goal KPI's. What could your team do with the time savings?</p>
  <div class="abs divider" style="top:764px"></div>
  <div class="abs svc-title" style="top:788px"><span class="accent">03</span> / Outcompete</div>
  <p class="abs svc-text" style="top:785px">Deliver results faster, gain performance insights, and leave a lasting impression on clients. Our mission is to create solutions that raise profitability while making your users and clients prefer you over the competition.</p>

  <!-- meet -->
  <h2 class="abs h2" style="left:0;width:795px;text-align:center;top:939px">Meet <span class="accent">Toucan</span></h2>
  <article class="abs card" style="left:75px">
    <svg width="30" height="30" viewBox="0 0 30 30" fill="none" stroke="var(--mist)" stroke-width="1.2"><rect x="4" y="3" width="22" height="16"/><path d="M8 8h14M8 12h10M15 19v8M10 27h10"/></svg>
    <h3>Our Story</h3>
    <p>We believe that technology can help businesses achieve more. That's why we've dedicated ourselves to creating software that truly empowers our clients.</p>
  </article>
  <article class="abs card feature" style="left:299px">
    <svg width="30" height="30" viewBox="0 0 30 30" fill="none" stroke="var(--umber)" stroke-width="1.2"><path d="M3 27h24M6 27V15h5v12M13 27V10h5v17M20 27V6h5v21"/><circle cx="15" cy="4" r="2"/></svg>
    <h3>Our Vision</h3>
    <p>Our vision is to help businesses of all sizes reach their full potential. We believe that by providing powerful, user-friendly software, we can help businesses become more efficient.</p>
  </article>
  <article class="abs card" style="left:522px">
    <svg width="30" height="30" viewBox="0 0 30 30" fill="none" stroke="var(--mist)" stroke-width="1.2"><path d="M15 5l11 6-11 6-11-6z M4 16l11 6 11-6 M4 21l11 6 11-6"/></svg>
    <h3>Our Software</h3>
    <p>Whether you're looking to streamline your processes, improve the client satisfaction, or boost your bottom line, our software can help.</p>
  </article>

  <!-- recent work -->
  <h2 class="abs h2" style="left:75px;top:1248px">Check Some of<br>Our <span class="accent">Recent Work</span></h2>
  <section class="abs panel" style="left:25px;top:1349px;width:744px;height:375px"></section>
  <div class="abs" style="left:75px;top:1435px"><span class="tag">Application</span><span class="tag">Industrial</span></div>
  <h3 class="abs work-title">BuildForge Industries:<br>Crafting Precision in Manufacturing<br>with Custom Software Solutions</h3>
  <p class="abs work-text">Lorem ipsum dolor sit amet, consectetur adipiscing elit, sed do eiusmod tempor incididunt ut labore et dolore magna aliqua. Quis ipsum suspendisse ultrices gravida.</p>
  <div class="abs features">
    <span><svg width="8" height="8" viewBox="0 0 8 8" fill="none" stroke="var(--lime)"><circle cx="4" cy="4" r="3.4"/><path d="M2.3 4l1.2 1.2L5.8 2.8"/></svg>Feature Goes Here</span>
    <span><svg width="8" height="8" viewBox="0 0 8 8" fill="none" stroke="var(--lime)"><circle cx="4" cy="4" r="3.4"/><path d="M2.3 4l1.2 1.2L5.8 2.8"/></svg>Feature Goes Here</span>
    <span><svg width="8" height="8" viewBox="0 0 8 8" fill="none" stroke="var(--lime)"><circle cx="4" cy="4" r="3.4"/><path d="M2.3 4l1.2 1.2L5.8 2.8"/></svg>Feature Goes Here</span>
  </div>
  <div class="abs arrow-btn" style="left:75px"><svg width="10" height="6" viewBox="0 0 10 6" fill="none" stroke="var(--mist)"><path d="M10 3H1M3 1L1 3l2 2"/></svg></div>
  <div class="abs arrow-btn on" style="left:111px"><svg width="10" height="6" viewBox="0 0 10 6" fill="none" stroke="var(--umber)"><path d="M0 3h9M7 1l2 2-2 2"/></svg></div>
  <div class="abs" style="left:423px;top:1398px;width:276px;height:276px;border-radius:50%;background:#3e2c21"></div>
  <svg class="abs" style="left:410px;top:1441px" width="303" height="186" viewBox="0 0 303 186">
    <rect x="26" y="2" width="251" height="166" rx="7" fill="#1a1a1a"/>
    <rect x="32" y="8" width="239" height="154" fill="#e9ebec" role="img" aria-label="Dashboard screenshot of the BuildForge app"/>
    <rect x="32" y="8" width="46" height="154" fill="#3a4046"/>
    <rect x="0" y="168" width="303" height="9" rx="4" fill="#cfd0d2"/>
    <rect x="120" y="168" width="63" height="4" fill="#a9aaac"/>
  </svg>

  <!-- clients -->
  <h2 class="abs h2" style="left:0;width:795px;text-align:center;top:1769px">Our <span class="accent">Clients</span></h2>
  <div class="abs client" style="left:75px"><i></i>CORVALE</div>
  <div class="abs client" style="left:200px"><i></i>LEVCO</div>
  <div class="abs client" style="left:316px">BRICKLINE</div>
  <div class="abs client" style="left:452px"><i></i>UPSET</div>
  <div class="abs client" style="left:550px">INFRO</div>
  <div class="abs client" style="left:660px">QUARRIO</div>

  <!-- testimonial -->
  <div class="abs quote-box"></div>
  <div class="abs photo" style="left:75px;top:1961px;width:166px;height:179px;background:linear-gradient(160deg,#9aa07a,#5d6b4a)" role="img" aria-label="Portrait of a smiling client in a checked shirt"></div>
  <svg class="abs" style="left:50px;top:1990px" width="48" height="34" viewBox="0 0 48 34" fill="var(--mist)"><path d="M0 16A14 14 0 0 1 14 2v6a8 8 0 0 0-6 6h6v18H0z M26 16A14 14 0 0 1 40 2v6a8 8 0 0 0-6 6h6v18H26z" transform="rotate(180 20 17)"/></svg>
  <p class="abs quote-text">"Toucan Studio has truly transformed our business with their exceptional custom software development services. Their team not only possesses a deep understanding of our industry but also a remarkable ability to translate our unique needs into innovative solutions. The tailored software they developed for us has streamlined our operations, increased efficiency, and enhanced overall productivity. Working with Toucan Studio has been a collaborative and rewarding experience, and we look forward to continuing this partnership for future projects. Their dedication to quality and attention to detail have made a significant impact on our success."</p>
  <div class="abs quote-name">Marco Dellaverde</div>
  <div class="abs" style="left:370px;top:2132px;width:300px;height:1px;background:#8ea21f"></div>
  <svg class="abs" style="left:684px;top:2126px" width="52" height="10" viewBox="0 0 52 10" fill="none" stroke="var(--umber)" stroke-width=".7">
    <path d="M5 .8l1.2 2.6 2.8.3-2.1 1.9.6 2.8L5 7 2.5 8.4l.6-2.8L1 3.7l2.8-.3z"/>
    <path transform="translate(10.5 0)" d="M5 .8l1.2 2.6 2.8.3-2.1 1.9.6 2.8L5 7 2.5 8.4l.6-2.8L1 3.7l2.8-.3z"/>
    <path transform="translate(21 0)" d="M5 .8l1.2 2.6 2.8.3-2.1 1.9.6 2.8L5 7 2.5 8.4l.6-2.8L1 3.7l2.8-.3z"/>
    <path transform="translate(31.5 0)" d="M5 .8l1.2 2.6 2.8.3-2.1 1.9.6 2.8L5 7 2.5 8.4l.6-2.8L1 3.7l2.8-.3z"/>
    <path transform="translate(42 0)" d="M5 .8l1.2 2.6 2.8.3-2.1 1.9.6 2.8L5 7 2.5 8.4l.6-2.8L1 3.7l2.8-.3z"/>
  </svg>

  <!-- blog -->
  <h2 class="abs h2" style="left:82px;top:2232px">From the Blog</h2>
  <div class="abs photo" style="left:75px;top:2297px;width:327px;height:224px;border-radius:3px;background:linear-gradient(120deg,#1c1c1c,#6e6e6e 60%,#2a2a2a)" role="img" aria-label="Close-up of code on a monitor"></div>
  <div class="abs mini-tag" style="left:75px;top:2541px">5-Minute Read <span class="tag">Optimization</span><span class="tag">Performance</span></div>
  <h3 class="abs" style="left:75px;top:2563px;font-size:14px;line-height:17.5px;font-weight:400">Code Optimization Strategies for a Seamless<br>High-Performance Applications</h3>

  <article class="abs post-side" style="top:2297px">
    <div class="abs thumb photo" role="img" aria-label="Developer working at a desk with monitors"></div>
    <div class="abs txt"><div class="mini-tag">5-Minute Read <span class="tag">Optimization</span></div><h4>A Guide to Scalable Architecture and Seamless Operation</h4></div>
  </article>
  <article class="abs post-side" style="top:2446px">
    <div class="abs thumb photo" role="img" aria-label="Team reviewing plans on a laptop"></div>
    <div class="abs txt"><div class="mini-tag">5-Minute Read <span class="tag">Optimization</span></div><h4>A Guide to Scalable Architecture and Seamless Operation</h4></div>
  </article>

  <!-- contact -->
  <section class="abs panel" style="left:25px;top:2642px;width:744px;height:392px"></section>
  <h2 class="abs h2" style="left:0;width:795px;text-align:center;top:2688px">Ready to <span class="accent">Launch</span> Your Project?<br>Let's Discuss</h2>
  <div class="abs field" style="left:99px;top:2786px;width:181px"><b>My name is*</b><span class="rule"></span></div>
  <div class="abs field" style="left:310px;top:2786px;width:179px"><b>I work for*</b><span class="rule"></span></div>
  <div class="abs field" style="left:510px;top:2786px;width:186px"><b>Email me at*</b><span class="rule"></span></div>
  <div class="abs field" style="left:99px;top:2826px;width:261px"><b>Call me at*</b><span class="rule"></span></div>
  <div class="abs field" style="left:391px;top:2826px;width:305px"><b>Type of service I need*</b><span class="rule"></span></div>
  <div class="abs field" style="left:99px;top:2867px;width:597px"><b>This is my inquiry</b><span class="rule"></span></div>
  <div class="abs go">LET'S GO!<svg width="9" height="9" viewBox="0 0 9 9" fill="var(--umber)"><path d="M0 4L9 0 5 9 4 5z"/></svg></div>

  <!-- footer -->
  <div class="abs brand" style="left:0;width:795px;justify-content:center;top:3088px;font-size:19px"><span class="dot" style="width:11px;height:11px"></span>Toucan</div>
  <div class="abs f-col" style="left:205px"><h5><span class="accent">-</span> Inquiries:</h5><p>avery@hiketoucan.net</p></div>
  <div class="abs f-col" style="left:328px"><h5><span class="accent">-</span> Call Us:</h5><p>555-014-2290</p></div>
  <div class="abs f-col" style="left:474px"><h5><span class="accent">-</span> Address:</h5><p>2218 Larkfield Ct<br>Denton, TX 76201</p></div>
  <div class="abs foot-small" style="left:75px">© 2024 ToucanStudio</div>
  <div class="abs social" style="left:363px"></div>
  <div class="abs social" style="left:388px"></div>
  <div class="abs social" style="left:413px"></div>
  <div class="abs foot-small" style="left:600px;width:120px;text-align:right">Privacy Policy | Terms of Use</div>
</main>
</body>
</html>
```